Electrical company needs professional eye catching business cards

I am an electrician who needs business cards. I have attached two images which you can use. The file ab.jpg I would atleast like to be used. The file named back.jpg can be used on the back or not... up to you.

The information on my business cards I will have displayed will be-
My name
Mobile number
web site url
Licence number
ABN

Also as another request, I would like the word "Electrician" on the front of the card somewhere. Maybe under my name or something?

Industry/Entity Type

Electrician

```html
<!DOCTYPE html>
<html lang="en">
<head>
<meta charset="utf-8">
<title>Norvale Installations – Business Cards</title>
<link href="https://fonts.googleapis.com/css2?family=Open+Sans:wght@400;600;700&display=swap" rel="stylesheet">
<style>
  :root {
    --backdrop: #2b2b2b;
    --card-blue: #213f9e;
    --card-ink: #ffffff;
    --card-shadow: rgba(0, 0, 0, 0.55);
  }
  * { margin: 0; padding: 0; box-sizing: border-box; }
  html, body {
    width: 1200px;
    height: 899px;
    overflow: hidden;
    background: var(--backdrop);
    font-family: "Open Sans", Arial, sans-serif;
    color: var(--card-ink);
  }
  .canvas {
    position: relative;
    width: 1200px;
    height: 899px;
  }
  .card {
    position: absolute;
    left: 315px;
    width: 570px;
    height: 345px;
    background: var(--card-blue);
    box-shadow: 0 14px 30px var(--card-shadow);
  }
  .card--front { top: 70px; }
  .card--back { top: 470px; }

  /* Front */
  .holder {
    position: absolute;
    left: 34px;
    top: 30px;
  }
  .holder__name {
    font-size: 19px;
    font-weight: 400;
    letter-spacing: 0.3px;
    line-height: 1.1;
  }
  .holder__name strong { font-weight: 700; }
  .holder__role {
    font-size: 14px;
    margin-left: 12px;
    line-height: 1.2;
  }
  .contact {
    position: absolute;
    left: 34px;
    bottom: 44px;
    line-height: 1.2;
  }
  .contact__mobile,
  .contact__web { font-size: 16px; }
  .contact__licence {
    font-size: 11px;
    letter-spacing: 0.3px;
    margin-top: 2px;
  }
  .brand-stack {
    position: absolute;
    right: 34px;
    top: 90px;
    display: flex;
    flex-direction: column;
    align-items: center;
  }
  .brand-mark {
    width: 78px;
    height: 62px;
    background: var(--card-ink);
    border-radius: 8px;
    margin-bottom: 10px;
  }
  .brand-name {
    font-size: 34px;
    font-weight: 600;
    line-height: 1;
    letter-spacing: -0.3px;
  }
  .brand-abn {
    font-size: 15px;
    margin-top: 4px;
  }

  /* Back */
  .brand-row {
    position: absolute;
    inset: 0;
    display: flex;
    align-items: center;
    justify-content: center;
    gap: 10px;
  }
  .brand-row .brand-mark {
    width: 92px;
    height: 72px;
    margin-bottom: 0;
  }
  .brand-row .brand-name {
    font-size: 44px;
  }
</style>
</head>
<body>
<main class="canvas">
  <section class="card card--front" aria-label="Card front">
    <div class="holder">
      <p class="holder__name"><strong>YOUR</strong> NAME</p>
      <p class="holder__role">Electrician</p>
    </div>
    <div class="contact">
      <p class="contact__mobile">Your Mobile number</p>
      <p class="contact__web">Web Site URL</p>
      <p class="contact__licence">LICENCE NUMBER</p>
    </div>
    <div class="brand-stack">
      <div class="brand-mark" aria-hidden="true"></div>
      <p class="brand-name">Norvale Installations</p>
      <p class="brand-abn">ABN</p>
    </div>
  </section>

  <section class="card card--back" aria-label="Card back">
    <div class="brand-row">
      <div class="brand-mark" aria-hidden="true"></div>
      <p class="brand-name">Norvale Installations</p>
    </div>
  </section>
</main>
</body>
</html>
```